Facebook Header Design Project.

I'm supplying white and colored logos. The Facebook page already exists. URL = https://www.examplesocial.test/lumacrest.design The design should not be based on what's already there. Consider mobile implications of the design. This Design will form the designs of other social media headers. LumaCrest is a web design | digital marketing company.

Target Market(s)

People interested in web design | digital marketing services.

Industry/Entity Type

LumaCrest is a web design | digital marketing company. That should be clear in the design.

Colors
0054AA
0677BA
7BADD7
CADEEF
E8F1F8

Requirements
Must have
• Logo. Use Facebook header image dimension.
Nice to have
• Use a color scheme like the logo and feel free to add a color or two from the other side of the color whee.

```html
<!DOCTYPE html>
<html lang="en">
<head>
<meta charset="utf-8">
<title>LumaCrest – Social Header</title>
<link rel="stylesheet" href="https://fonts.googleapis.com/css2?family=Outfit:wght@600;700&family=Montserrat:wght@600;700&display=swap">
<style>
  :root {
    --page: #fdfdfd;
    --ink: #1e222b;
    --cyan: #00bcf2;
    --accent-blue: #1e90e6;
    --white: #ffffff;
    --photo-top: #4d6278;
    --photo-mid: #2c3e52;
    --photo-bottom: #17222f;
  }
  * { box-sizing: border-box; margin: 0; padding: 0; }
  html, body {
    width: 1200px; height: 1200px; overflow: hidden;
    background: var(--page);
  }
  .header-banner {
    position: absolute;
    left: 118px; top: 424px;
    width: 972px; height: 359px;
    background: var(--ink);
    overflow: hidden;
    box-shadow: 0 10px 28px rgba(0,0,0,0.28);
  }
  .banner-shapes {
    position: absolute; inset: 0;
    width: 972px; height: 359px;
  }
  .brand {
    position: absolute;
    left: 46px; top: 52px;
    display: flex; align-items: center; gap: 10px;
  }
  .brand-mark {
    width: 18px; height: 18px;
    background: var(--cyan);
  }
  .brand-name {
    font-family: "Montserrat", sans-serif;
    font-weight: 700;
    font-size: 30px;
    color: var(--white);
    letter-spacing: 0.5px;
  }
  .headline {
    position: absolute;
    left: 46px; top: 116px;
    font-family: "Outfit", sans-serif;
    font-weight: 700;
    font-size: 43px;
    line-height: 45px;
    letter-spacing: -0.6px;
    color: var(--white);
    text-transform: uppercase;
  }
  .headline .highlight { color: var(--accent-blue); }
  .tagline {
    position: absolute;
    left: 46px; top: 214px;
    font-family: "Montserrat", sans-serif;
    font-weight: 600;
    font-size: 21px;
    line-height: 28px;
    letter-spacing: 0.9px;
    color: var(--white);
  }
  .social-handle {
    position: absolute;
    left: 47px; top: 310px;
    display: flex; align-items: center; gap: 9px;
    font-family: "Montserrat", sans-serif;
    font-weight: 700;
    font-size: 18px;
    letter-spacing: 2px;
    color: var(--ink);
  }
  .social-dot {
    width: 17px; height: 17px;
    border-radius: 50%;
    background: var(--ink);
  }
</style>
</head>
<body>
  <section class="header-banner">
    <svg class="banner-shapes" viewBox="0 0 972 359" xmlns="http://www.w3.org/2000/svg">
      <defs>
        <linearGradient id="cityGlow" x1="0" y1="0" x2="0" y2="1">
          <stop offset="0" stop-color="var(--photo-top)"/>
          <stop offset="0.5" stop-color="var(--photo-mid)"/>
          <stop offset="1" stop-color="var(--photo-bottom)"/>
        </linearGradient>
      </defs>
      <polygon class="accent-triangle" points="480.6,0 610.6,0 543.8,108.8" fill="var(--cyan)"/>
      <polygon class="city-photo" role="img" aria-label="Night city skyline with glowing digital network icons for mobile, payment and cloud"
               points="610.6,0 972,0 972,359 388.8,359" fill="url(#cityGlow)"/>
      <polygon class="corner-white" points="972,145 972,359 838.8,359" fill="var(--white)"/>
      <polygon class="corner-cyan" points="915,310.6 972,220 972,316.9 945,359" fill="var(--cyan)"/>
      <polygon class="handle-band" points="0,296.9 341.3,296.9 313.8,359 0,359" fill="var(--cyan)"/>
    </svg>

    <div class="brand">
      <span class="brand-mark"></span>
      <span class="brand-name">LumaCrest</span>
    </div>

    <h1 class="headline">
      <span class="highlight">We make</span> digital<br>
      marketing <span class="highlight">simple</span>
    </h1>

    <p class="tagline">Trusted by the world’s most<br>established brands.</p>

    <div class="social-handle">
      <span class="social-dot"></span>
      <span>@lumacrest.design</span>
    </div>
  </section>
</body>
</html>
```